Brivet Networks, Inc. Website redesign

Revamp the website, it is old and outdated. www.brivetnetworksinc.com

Target Market(s)

Information Technology Consulting and Staffing

Coding

Coded - Design and coding required

Number of Pages Required

5+ page

Colors

Designer to choose colors to be used in the design.

Requirements
Must have
• Outlined text boxes just like from the Hollis.us site. A clean look

```html
<!DOCTYPE html>
<html lang="en">
<head>
<meta charset="utf-8">
<title>Brivet Networks, Inc.</title>
<link href="https://fonts.googleapis.com/css2?family=Oswald:wght@500&family=Arimo:wght@400;700&display=swap" rel="stylesheet">
<style>
:root{
  --red:#d21c22;
  --red-light:#e65a45;
  --ink:#111111;
  --headline:#2b1414;
  --grey:#b5b5b5;
  --shadow:#e2e2e2;
  --white:#ffffff;
  --black:#121212;
}
*{margin:0;padding:0;box-sizing:border-box}
html,body{width:1200px;height:1200px;overflow:hidden;background:var(--white)}
body{position:relative;font-family:"Arimo",Arial,sans-serif}
.page-shadow{position:absolute;left:154px;top:41px;width:906px;height:1132px;background:var(--shadow)}
.page{position:absolute;left:147px;top:34px;width:906px;height:1132px;background:var(--white)}
.hero{position:absolute;left:0;top:0;width:906px;height:376px;background:linear-gradient(100deg,var(--red) 0%,#cf2226 55%,var(--red-light) 100%)}
.logo{position:absolute;left:63px;top:24px;color:var(--white);font-family:"Arimo",sans-serif;font-weight:700;font-size:33px;line-height:29px}
.nav{position:absolute;top:18px;left:0;list-style:none}
.nav li{position:absolute;white-space:nowrap;color:var(--white);font-family:"Oswald",sans-serif;font-size:20px;letter-spacing:-.2px}
.headline{position:absolute;left:63px;top:152px;width:400px;color:var(--headline);font-weight:700;font-size:24px;line-height:27px}
.intro{position:absolute;left:63px;top:220px;width:370px;color:var(--white);font-size:13.5px;line-height:16px}
.btn-learn{position:absolute;left:64px;top:298px;width:109px;height:34px;border-radius:17px;background:var(--white);color:var(--ink);font-family:"Oswald",sans-serif;font-size:17px;line-height:34px;text-align:center}
.about-text{position:absolute;left:68px;top:411px;width:300px;font-size:13.5px;line-height:15.8px;color:var(--ink)}
.photo{position:absolute}
.photo-climber{left:382px;top:404px;width:158px;height:104px;background:linear-gradient(160deg,#9aa7a8,#4c6460)}
.photo-road{left:382px;top:525px;width:158px;height:104px;background:linear-gradient(180deg,#6b7478,#3c3f3a 60%,#55502f)}
.photo-portrait{left:564px;top:404px;width:261px;height:224px;background:linear-gradient(180deg,#c8c6c2,#a9a6a2)}
.features{position:absolute;left:0;top:660px;width:906px;height:362px;background:var(--grey)}
.feature{position:absolute;top:60px;width:200px;text-align:center;color:var(--white);font-size:13.5px;line-height:15.8px}
.pill{display:inline-block;width:109px;height:34px;border-radius:17px;background:var(--white);color:var(--red);font-family:"Oswald",sans-serif;font-size:17px;line-height:34px}
.stem{width:1px;height:26px;background:#888;margin:6px auto 8px}
.feature a{color:var(--red);text-decoration:none}
.btn-read{display:block;margin:18px auto 0;width:66px;height:13px;border-radius:7px;background:var(--ink);color:var(--white);font-family:"Oswald",sans-serif;font-size:8px;line-height:13px}
.footer{position:absolute;left:0;top:1036px;width:906px;height:96px;background:var(--black);font-family:"Oswald",sans-serif;font-size:11.5px;color:var(--white)}
.footer-rule{position:absolute;left:51px;top:32px;width:812px;border-top:2px dotted #cfcfcf}
.copyright{position:absolute;left:61px;top:49px}
.copyright span{color:var(--red)}
.follow{position:absolute;left:711px;top:49px}
.divider{position:absolute;left:771px;top:50px;width:1px;height:14px;background:#555}
.social{position:absolute;top:52px;width:10px;height:10px;background:var(--red)}
</style>
</head>
<body>
<div class="page-shadow"></div>
<div class="page">
  <header class="hero" role="img" aria-label="Red-toned photo of a hiker leaping over a mountain ridge">
    <div class="logo">LOGO<br>IMAGE</div>
    <ul class="nav">
      <li style="left:351px">HOME</li>
      <li style="left:415px">ABOUT US</li>
      <li style="left:506px">SERVICES</li>
      <li style="left:588px">STRATEGIES</li>
      <li style="left:691px">IT NEWS</li>
      <li style="left:765px">CONTACT</li>
    </ul>
    <h1 class="headline">Bringning Thought Leadership and Quality to Every Project</h1>
    <p class="intro">Brivet Networks, Inc. is an&nbsp; 8(a) full-service IT consulting company based in Washington, DC Metro area. We offer specialized, highly customized technology solutions for our customers located throughout the United State.</p>
    <div class="btn-learn">LEARN MORE</div>
  </header>

  <p class="about-text">No two businesses are the same. We believe the technology supporting your business operations should align with your company. Every project begins with a thorough anaysis of your current technology environment. We work with you to define the environment you want. Then we implement industry-proven practices that enable you to achieve your business objectives. We draw on our experience at civilian and federal agenecies to generate ideas and create IT solutions that address your unique business needs.<br>Learn aboutour Strategies.</p>
  <div class="photo photo-climber" role="img" aria-label="Hiker with backpack jumping in the mountains"></div>
  <div class="photo photo-road" role="img" aria-label="Winding road through a mountain valley"></div>
  <div class="photo photo-portrait" role="img" aria-label="Portrait of a smiling young man in a suit and red tie"></div>

  <section class="features">
    <div class="feature" style="left:73px">
      <div class="pill">ABOUT US</div>
      <div class="stem"></div>
      <p>Brivet Networks, Inc. is an&nbsp; 8(a) full-service IT consulting company based in Washington, DC Metro area. We offer specialized, highly customized technology solutions for our customers located throughout the United State.</p>
    </div>
    <div class="feature" style="left:338px">
      <div class="pill">SERVICES</div>
      <div class="stem"></div>
      <p>Brivet Networks, Inc. organizes our Services into four key areas. While these four services can be implemented individually the majority of our orijects successfully combine components from each. Our people and our process is what makes us successful in providing theses services.</p>
      <span class="btn-read">READ MORE</span>
    </div>
    <div class="feature" style="left:607px">
      <div class="pill">CONTACT US</div>
      <div class="stem"></div>
      <p>555-010-2471 (Office) or send us an email.<br>Also you can visit our website.<br><a href="#">www.brivetnetworksinc.com</a></p>
    </div>
  </section>

  <footer class="footer">
    <div class="footer-rule"></div>
    <div class="copyright"><span>COPYRIGHT</span> BRIVET NETWORKS</div>
    <div class="follow">FOLLOW US</div>
    <div class="divider"></div>
    <div class="social" style="left:780px"></div>
    <div class="social" style="left:797px"></div>
  </footer>
</div>
</body>
</html>
```